Creative & Appealing Business Card

Required a business card for Ferndale Recoveries
We specialise in claims management services for PPI ( Payment Protection Insurance.
2 sided business card
Round Corners
I like embossed and raised lettering

Industry/Entity Type

Business

```html
<!DOCTYPE html>
<html lang="en">
<head>
<meta charset="utf-8">
<title>Ferndale Recoveries – Business Card</title>
<link rel="stylesheet" href="https://fonts.googleapis.com/css2?family=Open+Sans:wght@400;700&display=swap">
<style>
  :root {
    --ink: #000000;
    --paper: #ffffff;
    --backdrop: #9c9c9c;
    --text: #111111;
  }
  * { margin: 0; padding: 0; box-sizing: border-box; }
  html, body { width: 1200px; height: 900px; overflow: hidden; }
  body {
    background: var(--backdrop);
    font-family: "Open Sans", Arial, sans-serif;
    position: relative;
  }
  .card {
    position: absolute;
    left: 330px;
    width: 540px;
    height: 310px;
    border-radius: 16px;
    overflow: hidden;
    background: var(--paper);
    box-shadow: 0 6px 18px rgba(0,0,0,0.25);
  }
  .card--back { top: 115px; }
  .card--front { top: 475px; }

  .band { position: absolute; left: 0; width: 100%; background: var(--ink); }
  .card--back .band { top: 48px; height: 214px; }
  .card--front .band--top { top: 0; height: 120px; }
  .card--front .band--bottom { top: 282px; height: 18px; }

  .brand {
    position: absolute;
    display: flex;
    align-items: center;
    gap: 16px;
    color: var(--paper);
  }
  .brand__dot {
    width: 62px; height: 62px;
    border-radius: 50%;
    background: var(--paper);
    flex: none;
  }
  .brand__name {
    font-weight: 700;
    font-size: 30px;
    line-height: 1.02;
    text-transform: uppercase;
    letter-spacing: 0.5px;
  }
  .card--back .brand { left: 50%; top: 50%; transform: translate(-50%, -50%); }
  .card--front .brand { right: 36px; top: 26px; }
  .card--front .brand__dot { width: 52px; height: 52px; }
  .card--front .brand__name { font-size: 25px; }

  .holder {
    position: absolute;
    left: 30px; top: 140px;
    font-weight: 700;
    font-size: 18px;
    color: var(--text);
  }
  .contacts {
    position: absolute;
    right: 24px; top: 168px;
    list-style: none;
    text-align: right;
    font-size: 14px;
    line-height: 21px;
    color: var(--text);
  }
  .contacts li { display: flex; justify-content: flex-end; align-items: center; gap: 8px; }
  .contacts svg { width: 12px; height: 12px; fill: var(--ink); flex: none; }
</style>
</head>
<body>

<section class="card card--back" aria-label="Card back">
  <div class="band">
    <div class="brand">
      <span class="brand__dot"></span>
      <span class="brand__name">Ferndale<br>Recoveries</span>
    </div>
  </div>
</section>

<section class="card card--front" aria-label="Card front">
  <div class="band band--top">
    <div class="brand">
      <span class="brand__dot"></span>
      <span class="brand__name">Ferndale<br>Recoveries</span>
    </div>
  </div>
  <p class="holder">Daniel Marsh</p>
  <ul class="contacts">
    <li>+44 (0) 300 555 0148
      <svg viewBox="0 0 12 12"><path d="M1 4c0-2 2-2.5 5-2.5S11 2 11 4l-2 .5-.5-1.2h-5L3 4.5zM2.5 6h7l1 4.5h-9z"/></svg></li>
    <li>+44 (0) 207 946 0321
      <svg viewBox="0 0 12 12"><path d="M3 0.5h6a1 1 0 0 1 1 1v9a1 1 0 0 1-1 1H3a1 1 0 0 1-1-1v-9a1 1 0 0 1 1-1zM3.5 2v6.5h5V2z"/></svg></li>
    <li>daniel@ferndalerecoveries.com
      <svg viewBox="0 0 12 12"><path d="M0.5 2.5h11v7h-11zM1.5 3.5 6 6.8l4.5-3.3z" fill-rule="evenodd"/></svg></li>
    <li>www.ferndalerecoveries.com
      <svg viewBox="0 0 12 12"><path d="M4.5 7.5l3-3" stroke="#000" stroke-width="1.4"/><path d="M5 3.5l1.5-1.5a2.1 2.1 0 0 1 3 3L8 6.5M7 8.5 5.5 10a2.1 2.1 0 0 1-3-3L4 5.5" stroke="#000" stroke-width="1.4" fill="none"/></svg></li>
    <li>48 Ashgrove Lane London, N4 2PL
      <svg viewBox="0 0 12 12"><path d="M6 0.5a4 4 0 0 1 4 4c0 3-4 7-4 7s-4-4-4-7a4 4 0 0 1 4-4zm0 2.3a1.7 1.7 0 1 0 0 3.4 1.7 1.7 0 0 0 0-3.4z" fill-rule="evenodd"/></svg></li>
  </ul>
  <div class="band band--bottom"></div>
</section>

</body>
</html>
```